Attic Rivers (Progressive House Album)

Hey Guys,

I'm a music artist and I need a CD Cover done for my new album.The album is called "Attic Rivers" and I really need something artistic, almost like a painting that reflects the name of the album.

Also please feel free to step out from the whole "almost like a painting" box, if your inner creator has something else to say. But preferably I'd have it as a painting...

Here are some keywords: Deep, Progressive, Lucid Dreaming, Ocean, Bedroom...

Please listen to the 3:30 demo of the album to get a better idea.

Thanks,

RoJa

Update:

I've uploaded a few images to kinda help you with the mood/colour tone and direction of what I want, Also, the script writing (I've uploaded a few examples), do it in white colour (left to right, going little bit upwards), preferably on the bottom of the image, simple, one touch, thin hand writing. Have it fading in size (bigger to smaller) as you get to the end of each word. Just like when you sign something, but have it written in two lines.

The whole image should be deep in colour with sort of a glow effect.

Must have
• Name of the album with Script writing,
Should not have
• No paper mosaic art. Image pieced together with cut outs from different sources.

```html
<!DOCTYPE html>
<html lang="en">
<head>
<meta charset="utf-8">
<title>Attic Rivers — Album Cover</title>
<link rel="stylesheet" href="https://fonts.googleapis.com/css2?family=Pinyon+Script&display=swap">
<style>
  :root {
    --page: #ffffff;
    --ink: #ffffff;
    --violet: #6a4fc4;
    --indigo: #3b3fb0;
    --cyan: #4fc8e8;
    --magenta: #c04fb8;
    --rose: #d98aa8;
    --lilac: #b8a6e0;
    --plum: #4a2a6e;
  }
  * { margin: 0; padding: 0; box-sizing: border-box; }
  html, body {
    width: 1200px;
    height: 1200px;
    overflow: hidden;
    background: var(--page);
  }
  .canvas {
    position: relative;
    width: 1200px;
    height: 1200px;
    background: var(--page);
  }
  .cover {
    position: absolute;
    left: 120px;
    top: 122px;
    width: 960px;
    height: 960px;
    overflow: visible;
  }
  .cover-art {
    position: absolute;
    inset: 0;
    background:
      radial-gradient(circle at 50% 48%, var(--plum) 0%, transparent 22%),
      radial-gradient(circle at 52% 20%, var(--rose) 0%, transparent 28%),
      radial-gradient(circle at 82% 58%, var(--cyan) 0%, transparent 26%),
      radial-gradient(circle at 18% 62%, var(--magenta) 0%, transparent 24%),
      radial-gradient(circle at 20% 18%, var(--indigo) 0%, transparent 30%),
      radial-gradient(circle at 84% 16%, var(--violet) 0%, transparent 30%),
      radial-gradient(circle at 45% 82%, var(--indigo) 0%, transparent 30%),
      radial-gradient(circle at 80% 85%, var(--magenta) 0%, transparent 26%),
      linear-gradient(135deg, var(--lilac), var(--violet) 55%, var(--indigo));
  }
  .album-title {
    position: absolute;
    left: 0;
    top: 0;
    width: 100%;
    height: 100%;
    font-family: "Pinyon Script", cursive;
    color: var(--ink);
    font-weight: 400;
    line-height: 1;
    pointer-events: none;
  }
  .album-title .line {
    position: absolute;
    white-space: nowrap;
    transform-origin: left bottom;
    transform: rotate(-4deg);
  }
  .album-title .line-one {
    left: 40px;
    top: 70px;
    font-size: 290px;
  }
  .album-title .line-two {
    left: 200px;
    top: 330px;
    font-size: 290px;
  }
</style>
</head>
<body>
  <main class="canvas">
    <section class="cover">
      <div class="cover-art" role="img" aria-label="Painterly swirl of violet, cyan and pink liquid colour with translucent reaching hands layered over it"></div>
      <h1 class="album-title">
        <span class="line line-one">Attic</span>
        <span class="line line-two">Rivers</span>
      </h1>
    </section>
  </main>
</body>
</html>
```